Local Motorsports Photography Business Card Design

Looking for a Logo and Business Card design for my father who is a local photographer based in Perth operating under the business name "KLR Photography". Specializing in Motorsports (Torque Racers/Hyperwheels/Corvan Trial) and events photography.
Would like it to look professional, while still maintaining a local/personal feel. Color\Design of the Logo and Card are open to your own interpretation, but should limit the color scheme to around 2-3 colors.
Design should be a logo one side and contact details on the rear. The website currently is very simple and a generic template and should not be used as a basis for design.
Industry/Entity Type
Business
Contact Information for Business Card
Name: Malcolm Purdie
Website: www.klrphotography-example.com.au
Email: malcolm@klrphotography-example.com.au
Phone: 0471 629 385
Look and feel
Each slider illustrates characteristics of the customer's brand and the style your logo design should communicate.

```html
<!DOCTYPE html>
<html lang="en">
<head>
<meta charset="utf-8">
<title>KLR Photography – Business Card</title>
<link rel="stylesheet" href="https://fonts.googleapis.com/css2?family=Oswald:wght@300;400;500&display=swap">
<style>
  :root {
    --navy: #1e3f73;
    --sky: #3d8fd6;
    --yellow: #f2d21b;
    --grey: #6b6b6d;
    --white: #ffffff;
    --backdrop: #f2f2f2;
    --card-shadow: 0 10px 28px rgba(0,0,0,.18);
  }
  * { box-sizing: border-box; margin: 0; padding: 0; }
  html, body { width: 1200px; height: 873px; overflow: hidden; }
  body {
    background: var(--backdrop);
    font-family: "Oswald", "Arial Narrow", sans-serif;
    display: flex;
    align-items: center;
    justify-content: center;
    gap: 60px;
  }
  .card {
    position: relative;
    width: 520px;
    height: 297px;
    box-shadow: var(--card-shadow);
    overflow: hidden;
  }

  /* Contact side */
  .card--contact { background: var(--white); }
  .contact__header {
    position: absolute;
    top: 34px;
    left: 36px;
    line-height: 1.05;
  }
  .contact__header .person-name { color: var(--navy); font-size: 24px; font-weight: 400; letter-spacing: .5px; }
  .contact__header .person-role { color: #222; font-size: 15px; font-weight: 400; }
  .contact__divider {
    position: absolute; left: 0; right: 0; top: 162px; height: 18px;
    background: var(--grey);
    border-bottom: 5px solid var(--yellow);
  }
  .contact__band {
    position: absolute; left: 0; right: 0; top: 180px; bottom: 0;
    background: var(--navy);
  }
  .contact-list {
    position: absolute; top: 14px; left: 22px;
    list-style: none;
  }
  .contact-list li {
    display: flex; align-items: center; gap: 10px;
    color: var(--sky); font-size: 15px; font-weight: 300;
    height: 24px; letter-spacing: .3px;
  }
  .contact-list svg { width: 15px; height: 15px; fill: var(--sky); flex: none; }
  .band-signature {
    position: absolute; right: 24px; bottom: 16px; text-align: right; line-height: 1.05;
  }
  .band-signature .person-name { color: var(--white); font-size: 26px; font-weight: 400; letter-spacing: .5px; }
  .band-signature .person-role { color: var(--yellow); font-size: 17px; font-weight: 400; }

  /* Brand side */
  .card--brand {
    background: var(--navy);
    display: flex; flex-direction: column; align-items: center; justify-content: center;
    text-align: center; gap: 10px;
  }
  .brand__name { color: var(--white); font-size: 40px; font-weight: 400; letter-spacing: 1px; }
  .brand__tagline { color: var(--yellow); font-size: 15px; font-weight: 300; letter-spacing: .3px; }
  .brand__web { color: var(--sky); font-size: 15px; font-weight: 300; margin-top: 14px; }
</style>
</head>
<body>
  <section class="card card--contact" aria-label="Business card, contact side">
    <div class="contact__header">
      <div class="person-name">MALCOLM PURDIE</div>
      <div class="person-role">PRESIDENTE / CEO</div>
    </div>
    <div class="contact__divider"></div>
    <div class="contact__band">
      <ul class="contact-list">
        <li>
          <svg viewBox="0 0 24 24" aria-hidden="true"><path d="M6.6 10.8a15.1 15.1 0 0 0 6.6 6.6l2.2-2.2c.3-.3.7-.4 1-.2 1.1.4 2.3.6 3.6.6.6 0 1 .4 1 1V20c0 .6-.4 1-1 1C10.6 21 3 13.4 3 4c0-.6.4-1 1-1h3.5c.6 0 1 .4 1 1 0 1.3.2 2.5.6 3.6.1.3 0 .7-.2 1z"/></svg>
          0471 629 385
        </li>
        <li>
          <svg viewBox="0 0 24 24" aria-hidden="true"><path d="M2 5h20v14H2zM4 7v.5l8 5 8-5V7l-8 5z"/></svg>
          malcolm@klrphotography-example.com.au
        </li>
        <li>
          <svg viewBox="0 0 24 24" aria-hidden="true"><path d="M12 2a10 10 0 1 0 0 20 10 10 0 0 0 0-20zm6.9 6h-3a15 15 0 0 0-1.3-4A8 8 0 0 1 18.9 8zM12 4c.8 1.2 1.5 2.5 1.9 4h-3.8c.4-1.5 1.1-2.8 1.9-4zM4.3 14a8 8 0 0 1 0-4h3.4a16 16 0 0 0 0 4zm.8 2h3a15 15 0 0 0 1.3 4A8 8 0 0 1 5.1 16zm3-8h-3a8 8 0 0 1 4.3-4 15 15 0 0 0-1.3 4zM12 20c-.8-1.2-1.5-2.5-1.9-4h3.8c-.4 1.5-1.1 2.8-1.9 4zm2.3-6H9.7a14 14 0 0 1 0-4h4.6a14 14 0 0 1 0 4zm.3 6a15 15 0 0 0 1.3-4h3a8 8 0 0 1-4.3 4zm1.7-6a16 16 0 0 0 0-4h3.4a8 8 0 0 1 0 4z"/></svg>
          www.klrphotography-example.com.au
        </li>
      </ul>
      <div class="band-signature">
        <div class="person-name">MALCOLM PURDIE</div>
        <div class="person-role">PRESIDENTE / CEO</div>
      </div>
    </div>
  </section>

  <section class="card card--brand" aria-label="Business card, brand side">
    <h1 class="brand__name">KLR PHOTOGRAPHY</h1>
    <p class="brand__tagline">Specializing in Motorsports (Torque Racers/Hyperwheels/Corvan Trial)</p>
    <p class="brand__web">www.klrphotography-example.com.au</p>
  </section>
</body>
</html>
```